Horseracing 8 page brochure - tight turnaround, deadline tomorrow 12GMT

Hi - we have a brochure already drafted for our annual open day at our horseracing stables in England, but it needs a professional design please! The design should convey that this is a smart, professional yard. We brand in a dark blue (as seen on the logo on the back page) and shades of blue. We have a range of other landscape / action photos available. This needs an almost instant turnaround please

Target Market(s)

Racehorse owners - current and prospective. High net worth / socio economic group

Industry/Entity Type

It Professional

Other font styles liked:
• As per 'Owen Darby' text

Colors
0255a3
3176b5
85abd2
cedeed

Requirements
Must have
• All text and images in publisher file provided below. Other photos are optional for space filling / backrounds

```html
<!DOCTYPE html>
<html lang="en">
<head>
<meta charset="utf-8">
<title>Chalkridge Racing – Annual Open Day Brochure</title>
<link rel="stylesheet" href="https://fonts.googleapis.com/css2?family=Arvo:wght@400;700&family=Crimson+Text&family=Arimo&display=swap">
<style>
  :root {
    --navy: #2b1d66;
    --navy-deep: #2c1c63;
    --navy-light: #283a85;
    --swoosh: #c3c7cf;
    --page-edge: #d9d9d9;
    --ink: #222222;
    --white: #ffffff;
  }
  html, body {
    margin: 0;
    width: 1200px;
    height: 900px;
    overflow: hidden;
    background: var(--white);
  }
  .spread {
    position: relative;
    width: 1200px;
    height: 900px;
  }
  .page {
    position: absolute;
    top: 89px;
    width: 557px;
    height: 720px;
    overflow: hidden;
    box-sizing: border-box;
  }
  .page--back { left: 43px; border: 1px solid var(--page-edge); border-right: none; }
  .page--front { left: 600px; border: 1px solid var(--page-edge); border-left: none; }
  .page svg.page-art { position: absolute; inset: 0; }

  .notes-title {
    position: absolute;
    top: 266px;
    left: 0;
    width: 100%;
    text-align: center;
    font: 16px "Arimo", sans-serif;
    color: var(--ink);
    margin: 0;
  }
  .brand {
    display: flex;
    align-items: center;
    gap: 8px;
    font-family: "Crimson Text", serif;
    color: var(--navy);
  }
  .brand-mark {
    width: 14px;
    height: 14px;
    background: var(--navy);
    flex: none;
  }
  .back-brand {
    position: absolute;
    left: 42px;
    top: 610px;
    font-size: 20px;
  }
  .back-address {
    position: absolute;
    left: 42px;
    top: 648px;
    margin: 0;
    font: 10px/1.15 "Arimo", sans-serif;
    color: var(--ink);
    font-style: normal;
  }
  .back-contact {
    position: absolute;
    left: 362px;
    top: 623px;
    margin: 0;
    font: 10.5px/1.2 "Arimo", sans-serif;
    color: var(--ink);
  }
  .back-contact .web { padding-left: 12px; }

  .front-tab {
    position: absolute;
    top: 26px;
    right: 0;
    width: 296px;
    height: 74px;
    background: var(--white);
    clip-path: polygon(0 0, 100% 0, 100% 100%, 0 100%, 34px 50%);
  }
  .front-brand {
    position: absolute;
    left: 36px;
    top: 12px;
    font-size: 20px;
    line-height: 1.2;
    gap: 12px;
  }
  .front-date {
    position: absolute;
    top: 582px;
    left: 0;
    width: 100%;
    text-align: center;
    margin: 0;
    font: 700 17px "Arvo", serif;
    color: var(--white);
  }
  .front-title {
    position: absolute;
    top: 608px;
    left: 0;
    width: 100%;
    text-align: center;
    margin: 0;
    font: 400 50px "Arvo", serif;
    color: var(--white);
    letter-spacing: 0.5px;
  }
</style>
</head>
<body>
<main class="spread">

  <section class="page page--back">
    <svg class="page-art" width="557" height="720" viewBox="0 0 557 720">
      <defs>
        <linearGradient id="downsLandscape" x1="0" y1="0" x2="0" y2="1">
          <stop offset="0" stop-color="#4d5460"/>
          <stop offset="0.28" stop-color="#8a9196"/>
          <stop offset="0.4" stop-color="#6f8a45"/>
          <stop offset="1" stop-color="#5d8f2e"/>
        </linearGradient>
      </defs>
      <path class="swoosh" fill="var(--swoosh)" d="M0,165 C160,225 400,218 557,182 L557,190 C400,245 180,255 0,185 Z"/>
      <path role="img" aria-label="Photo of rolling green downland with a wooden trail signpost under a stormy sky"
            fill="url(#downsLandscape)" d="M0,0 H557 V182 C400,218 160,225 0,165 Z"/>
    </svg>

    <h2 class="notes-title">Notes</h2>

    <div class="brand back-brand"><span class="brand-mark"></span>Chalkridge Racing Ltd</div>
    <address class="back-address">Lower Fernhill Farm, Ashcombe, Hartley<br>Westbury, Wiltshire, SN9 2XT</address>
    <p class="back-contact">Phone: 01632 960418<br>Mobile: 07700 900512<br>E-mail: owen@owen-darby.co.uk<br><span class="web">www.owen-darby.co.uk</span></p>
  </section>

  <section class="page page--front">
    <svg class="page-art" width="557" height="720" viewBox="0 0 557 720">
      <defs>
        <linearGradient id="coverNavy" x1="0" y1="0" x2="0" y2="1">
          <stop offset="0" stop-color="var(--navy-deep)"/>
          <stop offset="1" stop-color="var(--navy-light)"/>
        </linearGradient>
        <linearGradient id="raceAction" x1="0" y1="0" x2="1" y2="1">
          <stop offset="0" stop-color="#4f8a48"/>
          <stop offset="0.45" stop-color="#9a6a45"/>
          <stop offset="0.7" stop-color="#b0a79c"/>
          <stop offset="1" stop-color="#6f9a52"/>
        </linearGradient>
      </defs>
      <rect x="0" y="440" width="557" height="280" fill="url(#coverNavy)"/>
      <path class="swoosh" fill="var(--swoosh)" d="M0,478 C160,560 400,555 557,482 L557,498 C400,575 170,580 0,492 Z"/>
      <path role="img" aria-label="Photo of a chestnut racehorse and jockey galloping past a big screen at a racecourse"
            fill="url(#raceAction)" d="M0,0 H557 V482 C400,555 160,560 0,478 Z"/>
    </svg>

    <div class="front-tab">
      <div class="brand front-brand"><span class="brand-mark"></span><span>Owen Darby<br>Chalkridge Racing Ltd</span></div>
    </div>

    <p class="front-date">Sunday 11th September 2016</p>
    <h1 class="front-title">Annual Open day</h1>
  </section>

</main>
</body>
</html>
```